Tovrel Business Card

We are a modern retail clothing store. Established in 1994. I need a presentable card that will amaze vendors when given to them.

Front: Logo in middle
Info Side:

Name: Omar Latif
Cell: 630-555-0148
Work: 630-555-0192 EXT. 230
Email: Omar@tovrel.example
Website: www.Tovrel.example

Industry/Entity Type

Business

```html
<!DOCTYPE html>
<html lang="en">
<head>
<meta charset="utf-8">
<title>Tovrel Business Card</title>
<link rel="stylesheet" href="https://fonts.googleapis.com/css2?family=Montserrat:wght@400;600&display=swap">
<style>
  :root {
    --frame: #1d1f20;
    --card: #0f1112;
    --divider: #050606;
    --ink: #f1f3f1;
  }
  html, body {
    margin: 0;
    padding: 0;
    width: 1200px;
    height: 725px;
    overflow: hidden;
    background: var(--frame);
  }
  .card {
    position: relative;
    width: 1200px;
    height: 725px;
    background: var(--frame);
    font-family: "Montserrat", sans-serif;
    color: var(--ink);
  }
  .card-face {
    position: absolute;
    left: 19px;
    top: 20px;
    right: 16px;
    bottom: 17px;
    background: var(--card);
  }
  .brand-name {
    position: absolute;
    left: 162px;
    top: 326px;
    margin: 0;
    font-size: 64px;
    font-weight: 600;
    letter-spacing: 4px;
    line-height: 1;
    color: var(--ink);
  }
  .divider {
    position: absolute;
    left: 600px;
    top: 119px;
    width: 3px;
    height: 487px;
    background: var(--divider);
  }
  .contact-list {
    position: absolute;
    left: 692px;
    top: 0;
    margin: 0;
    padding: 0;
    list-style: none;
  }
  .contact-item {
    position: absolute;
    left: 0;
    display: flex;
    align-items: flex-start;
    white-space: nowrap;
  }
  .contact-icon {
    width: 30px;
    height: 30px;
    flex: none;
    fill: var(--ink);
  }
  .contact-text {
    margin-left: 47px;
    font-size: 28px;
    font-weight: 400;
    line-height: 33px;
    letter-spacing: 0.5px;
  }
  .item-name  { top: 184px; }
  .item-email { top: 280px; }
  .item-web   { top: 380px; }
  .item-phone { top: 481px; }
</style>
</head>
<body>
<div class="card">
  <div class="card-face">
  </div>
  <h1 class="brand-name">TOVREL</h1>
  <div class="divider"></div>
  <ul class="contact-list">
    <li class="contact-item item-name">
      <svg class="contact-icon" viewBox="0 0 30 30" aria-hidden="true">
        <path d="M15 2c-4 0-6 3-6 7s2.5 8 6 8 6-4 6-8-2-7-6-7z"/>
        <path d="M2 29c0-6 4-9 9-10l4 3 4-3c5 1 9 4 9 10z"/>
      </svg>
      <span class="contact-text">Omar Latif</span>
    </li>
    <li class="contact-item item-email">
      <svg class="contact-icon" viewBox="0 0 30 30" aria-hidden="true">
        <path d="M1 6h28v19H1z M3.5 8v15h23V8L15 18z M4.5 7.5L15 16 25.5 7.5z" fill-rule="evenodd"/>
      </svg>
      <span class="contact-text">Omar@tovrel.example</span>
    </li>
    <li class="contact-item item-web">
      <svg class="contact-icon" viewBox="0 0 30 30" aria-hidden="true">
        <circle cx="15" cy="15" r="13" fill="none" stroke="#f1f3f1" stroke-width="2.5"/>
        <path d="M8 8c3-1 5 1 7 0 1 2-1 4-3 4-1 2 1 4-1 6-2-1-3-4-5-5 0-2 1-3 2-5z"/>
        <path d="M18 16c2-1 4 0 5 2-1 3-3 5-5 6-1-2 0-4-1-5z"/>
        <path d="M19 6c2 0 4 1 5 3-2 0-3 1-4 0z"/>
      </svg>
      <span class="contact-text">www.Tovrel.example</span>
    </li>
    <li class="contact-item item-phone">
      <svg class="contact-icon" viewBox="0 0 30 30" aria-hidden="true">
        <path d="M6 2l5 6-3 4c2 4 6 8 10 10l4-3 6 5-4 4C13 27 3 17 2 6z"/>
      </svg>
      <span class="contact-text">630-555-0148<br>630-555-0192 EXT. 230</span>
    </li>
  </ul>
</div>
</body>
</html>
```